Business Card Design Project

I require a business card design that looks professional for a small building company. Calloway Builders is the name of the company and i don't want to use a house or building design for a logo. I require a logo design for the card incorporating the name Calloway Builders but designed smartly.

We are a Registered Building Practitioner so the small logo attached must also be used on the card.

We cover a large range of Building / Construction, Concrete, Steelwork. Not sure how to implement this.

Colors are flexible, maybe a dark grey background with white writting over it, but i am keen to see other options.

Thanks.

Target Market(s)

Anyone

Industry/Entity Type

Building

Requirements
Must have
• The logo attached must be incorporated - can be small
A logo for my company needs to be included - using Calloway Builders as the base with no picture of a house or buildings.

```html
<!DOCTYPE html>
<html lang="en">
<head>
<meta charset="utf-8">
<title>Calloway Builders – Business Card</title>
<link href="https://fonts.googleapis.com/css2?family=Archivo+Black&family=Russo+One&display=swap" rel="stylesheet">
<style>
  :root {
    --navy: #0a1628;
    --charcoal: #4d4d4d;
    --gap: #ffffff;
    --ink: #ffffff;
    --badge-line: #d9d9d9;
  }
  * { margin: 0; padding: 0; box-sizing: border-box; }
  html, body {
    width: 995px;
    height: 1200px;
    overflow: hidden;
    background: var(--gap);
  }
  .canvas {
    position: relative;
    width: 995px;
    height: 1200px;
  }
  .card {
    position: absolute;
    left: 0;
    width: 995px;
    height: 588px;
    color: var(--ink);
  }
  .card--navy { top: 0; background: var(--navy); }
  .card--charcoal { top: 612px; background: var(--charcoal); }

  .registration-badge {
    position: absolute;
    left: 36px;
    top: 49px;
    width: 90px;
    height: 90px;
    display: block;
  }

  .wordmark {
    position: absolute;
    left: 0;
    width: 100%;
    text-align: center;
    text-transform: uppercase;
    font-weight: 400;
  }
  .card--navy .wordmark {
    top: 340px;
    font-family: "Russo One", sans-serif;
    font-size: 54px;
    letter-spacing: 1px;
    line-height: 1;
  }
  .card--charcoal .wordmark {
    top: 290px;
    font-family: "Archivo Black", sans-serif;
    line-height: 0.86;
  }
  .wordmark__line { display: block; }
  .wordmark__line--upper { font-size: 66px; letter-spacing: 1px; }
  .wordmark__line--lower { font-size: 92px; letter-spacing: -1px; }

  .services {
    position: absolute;
    left: 0;
    width: 100%;
    display: flex;
    justify-content: center;
    align-items: center;
    text-transform: uppercase;
    list-style: none;
  }
  .services__item { display: flex; align-items: center; }
  .services__item + .services__item::before {
    content: "";
    display: inline-block;
    width: 2px;
    background: var(--ink);
  }
  .card--navy .services {
    top: 500px;
    font-family: "Russo One", sans-serif;
    font-size: 30px;
    letter-spacing: 0.5px;
  }
  .card--navy .services__item + .services__item::before { height: 20px; margin: 0 10px; }
  .card--charcoal .services {
    top: 508px;
    font-family: "Archivo Black", sans-serif;
    font-size: 22px;
    letter-spacing: 1.2px;
  }
  .card--charcoal .services__item + .services__item::before { height: 15px; margin: 0 12px; }
</style>
</head>
<body>
<main class="canvas">

  <section class="card card--navy" aria-label="Business card, navy version">
    <svg class="registration-badge" viewBox="0 0 90 90" role="img" aria-label="Registration badge">
      <circle cx="45" cy="45" r="43" fill="none" stroke="var(--badge-line)" stroke-width="2"/>
    </svg>
    <h1 class="wordmark">Calloway Builders</h1>
    <ul class="services">
      <li class="services__item">Building</li>
      <li class="services__item">Construction</li>
      <li class="services__item">Concrete</li>
      <li class="services__item">Steelwork</li>
    </ul>
  </section>

  <section class="card card--charcoal" aria-label="Business card, charcoal version">
    <svg class="registration-badge" viewBox="0 0 90 90" role="img" aria-label="Registration badge">
      <circle cx="45" cy="45" r="43" fill="none" stroke="var(--badge-line)" stroke-width="2"/>
    </svg>
    <h2 class="wordmark">
      <span class="wordmark__line wordmark__line--upper">Calloway</span>
      <span class="wordmark__line wordmark__line--lower">Builders</span>
    </h2>
    <ul class="services">
      <li class="services__item">Building</li>
      <li class="services__item">Construction</li>
      <li class="services__item">Concrete</li>
      <li class="services__item">Steelwork</li>
    </ul>
  </section>

</main>
</body>
</html>
```